" Serviço público e privado Formação e qualificação profissional em gestão e Gerenciamento de Projetos Gestão de projetos Mapeamento de processos Mediação de parcerias Inovação tecnológica Suporte de logistica e suprimentos Consultorias técnicas sem limitação de áreas de atuação. Produção de conhecimento Publicações e edições de livros, revistas e periódicos Desenvolvimento de protótipos Desenvolvimento de sistemas, serviços inovadores, aplicativos de inteligência mobile. Construção e gestão de parceria. Construção e desenvolvimento de portfólio de serviços Desenvolvimento e apóio à tecnologias sociais inovadoras Constução, desenvolvimento de planejamento estratégico Assessoria em desenvolvimento institucional integrado Desenvolvimento e aplicação de pesquisas Atuar na área de responsabilidade sócio-ambiental "

```html
<!DOCTYPE html>
<html lang="pt-BR">
<head>
<meta charset="UTF-8">
<title>Lumenar Consultoria – Cartão de Visita</title>
<link rel="stylesheet" href="https://fonts.googleapis.com/css2?family=Montserrat:wght@400;600;700&family=Open+Sans:wght@400;600&display=swap">
<style>
  :root {
    --stage: #e9e9e9;
    --card-dark: #1c1a19;
    --card-dark-edge: #2e2b29;
    --card-light: #ffffff;
    --orange: #f39a1e;
    --orange-deep: #e47c12;
    --text-light: #ffffff;
    --text-dark: #1f1f1f;
  }
  * { margin: 0; padding: 0; box-sizing: border-box; }
  html, body {
    width: 1200px;
    height: 1200px;
    overflow: hidden;
    background: var(--stage);
  }
  .sheet {
    position: relative;
    width: 1200px;
    height: 1200px;
  }
  .card {
    position: absolute;
    left: 150px;
    width: 900px;
    height: 500px;
    border-radius: 6px;
    box-shadow: 0 10px 28px rgba(0,0,0,0.18);
    overflow: hidden;
  }

  /* Front side */
  .card--front {
    top: 70px;
    background: radial-gradient(ellipse at 30% 60%, var(--card-dark-edge) 0%, var(--card-dark) 70%);
  }
  .brand {
    position: absolute;
    top: 78px;
    right: 80px;
    display: flex;
    align-items: center;
    gap: 18px;
  }
  .brand__dot {
    width: 34px;
    height: 34px;
    border-radius: 50%;
    background: var(--orange);
  }
  .brand__name {
    font-family: 'Montserrat', sans-serif;
    font-weight: 400;
    font-size: 46px;
    letter-spacing: 2px;
    color: var(--text-light);
    text-transform: uppercase;
    line-height: 1.05;
  }
  .person {
    position: absolute;
    top: 300px;
    right: 80px;
    text-align: right;
    font-family: 'Montserrat', sans-serif;
  }
  .person__name {
    font-weight: 600;
    font-size: 27px;
    color: var(--orange);
    text-transform: uppercase;
    letter-spacing: 0.5px;
  }
  .person__role {
    margin-top: 8px;
    font-weight: 600;
    font-size: 25px;
    color: var(--text-light);
  }

  /* Back side */
  .card--back {
    top: 630px;
    background: var(--card-light);
  }
  .tab {
    position: absolute;
    width: 22px;
    height: 110px;
    background: linear-gradient(90deg, var(--orange-deep), var(--orange));
  }
  .tab--left { left: 0; top: 300px; border-radius: 0 14px 14px 0; }
  .tab--right { right: 0; top: 110px; border-radius: 14px 0 0 14px; }
  .contact {
    position: absolute;
    font-family: 'Open Sans', sans-serif;
    font-weight: 600;
    font-size: 24px;
    line-height: 1.35;
    color: var(--text-dark);
  }
  .contact--web { top: 100px; right: 80px; text-align: right; }
  .contact--phone { top: 230px; left: 80px; }
  .contact--address { top: 360px; left: 330px; }
</style>
</head>
<body>
<main class="sheet">
  <section class="card card--front" aria-label="Frente do cartão">
    <div class="brand">
      <span class="brand__dot"></span>
      <span class="brand__name">Lumenar<br>Consultoria</span>
    </div>
    <div class="person">
      <p class="person__name">Marina Teles</p>
      <p class="person__role">Diretora</p>
    </div>
  </section>

  <section class="card card--back" aria-label="Verso do cartão">
    <span class="tab tab--left"></span>
    <span class="tab tab--right"></span>
    <p class="contact contact--web">contato@lumenar.com.br<br>www.lumenar.com.br</p>
    <p class="contact contact--phone">(11) 3847-2200<br>(11) 3847-2201</p>
    <p class="contact contact--address">Rua das Acácias, 284 | Bairro<br>Cidade/UF | CEP: 04512-130</p>
  </section>
</main>
</body>
</html>
```